PowerPoint template design needed for sales and presales presentations

We would like to have a bright and light, contemporary PowerPoint design based on our existing style assets (see attached files).
We are based in Latvia. Our business is ERP systems implementation, IT infrastructure building and supporting our customers. We are moving from traditional Add-hoc projects model to standardized flat-rate offerings. Our technology platform is Quintavel.
The value proposition of our offerings is based around simplicity, transparency, quality, peace of mind, trust, easy of doing business.
I have to add that if any special are being used, they must be unicode to ensure proper Latvian language characters display.
Updates
Hi! The reason is an error at your side. Today it's 24/08/2020 when I started the project and made a payment. Still for some funny reason in the BRIEF I see that the project deadline is set to 20/08/2020. No wonder no designers are applying...
Target Market(s)
Small and medium enterprise
Look and feel

```html
<!DOCTYPE html>
<html lang="en">
<head>
<meta charset="utf-8">
<title>Lumara – Presentation Template</title>
<link href="https://fonts.googleapis.com/css2?family=Lato:wght@400;700;900&display=swap" rel="stylesheet">
<style>
:root{
  --green:#8cc63f;
  --green-d:#6fae2a;
  --green-l:#b5dc7a;
  --yellow:#f4c51c;
  --teal:#3fc6bd;
  --ink:#1f1f1f;
  --grey:#6d6d6d;
  --paper:#ffffff;
}
*{box-sizing:border-box;margin:0;padding:0}
html,body{width:1200px;height:4587px;overflow:hidden;background:#fff;font-family:"Lato",sans-serif;color:var(--ink)}
.canvas{position:relative;width:1200px;height:4587px}
.slide{position:absolute;width:549px;height:310px;overflow:hidden;background:var(--paper);box-shadow:2px 3px 8px rgba(0,0,0,.18)}
.col-l{left:39px}.col-r{left:607px}
.photo-night{background:radial-gradient(circle at 50% 70%,#7fb7c9 0%,#2f6f86 25%,#123a52 55%,#06182a 100%)}
.photo-dusk{background:linear-gradient(180deg,#3e5f66 0%,#c9b24a 45%,#7a8a3a 70%,#3b4a2a 100%)}
.photo-city{background:linear-gradient(180deg,#3a3d4a 0%,#6b6a6e 50%,#2e2f35 100%)}
.photo-team{background:linear-gradient(135deg,#d8d3c8 0%,#a98f73 45%,#5b6a7a 100%)}
.photo-teal{background:linear-gradient(135deg,#7fc3c0 0%,#3d8f94 60%,#2a6b70 100%)}
.brand{position:absolute;display:flex;align-items:center;font-weight:700;line-height:1;white-space:nowrap}
.brand .mark{display:block;border:2px solid currentColor;flex:none}
.brand-mini{position:absolute;top:10px;right:12px;display:flex;align-items:center;gap:3px;font-size:7px;font-weight:700;line-height:1}
.brand-mini .mark{width:6px;height:6px;border:1px solid currentColor;display:block}
.title{position:absolute;left:24px;top:22px;font-size:16px;font-weight:900}
.accent{position:absolute;width:22px}
.accent i{display:block;height:3px;margin-bottom:2px}
.accent .a1{background:var(--green);width:22px}
.accent .a2{background:var(--yellow);width:16px}
.accent .a3{background:var(--teal);width:10px}
.acc-tl{left:12px;top:10px}
.acc-br{right:10px;bottom:6px;transform:rotate(180deg)}
.body{font-size:6.5px;line-height:1.45;color:var(--grey)}
.abs{position:absolute}
.num{position:absolute;width:20px;height:20px;border-radius:50%;border:1.5px solid #fff;color:#fff;font-size:10px;font-weight:700;display:flex;align-items:center;justify-content:center}
.check{display:flex;align-items:center;gap:5px;font-size:6px;color:var(--ink);margin-bottom:9px}
.check b{width:9px;height:9px;border-radius:50%;background:var(--green);flex:none;position:relative}
.check b.dark{background:var(--ink)}
.check b::after{content:"";position:absolute;left:2.5px;top:1.5px;width:3px;height:4.5px;border:solid #fff;border-width:0 1.2px 1.2px 0;transform:rotate(45deg)}
table.fin{border-collapse:collapse;font-size:5.5px;width:100%}
table.fin td{padding:2px 4px;text-align:center;border-bottom:1px solid #e3e3e3}
table.fin tr.h td{background:var(--green);color:var(--ink);font-weight:700}
table.fin tr.t td{background:var(--teal);color:#fff;font-weight:700}
.proc{position:absolute;height:18px;font-size:6px;font-weight:700;display:flex;align-items:center;justify-content:center;color:#fff}
</style>
</head>
<body>
<div class="canvas">

<!-- Cover A -->
<section class="slide" style="left:39px;top:32px;width:1117px;height:626px;background:var(--green)">
  <svg class="abs" style="left:0;top:0" width="1117" height="626">
    <ellipse cx="330" cy="300" rx="360" ry="330" fill="#a6d45c" opacity=".8"/>
    <path d="M60 520 Q150 640 330 600 L60 626 Z" fill="var(--yellow)" opacity=".7"/>
    <circle cx="250" cy="350" r="240" fill="var(--yellow)" opacity=".55"/>
  </svg>
  <div class="abs photo-night" role="img" aria-label="Night aerial view of a city with lit highway interchanges" style="left:44px;top:97px;width:494px;height:494px;border-radius:50%"></div>
  <div class="brand" style="left:620px;top:262px;font-size:34px;color:#fff;gap:12px"><span class="mark" style="width:28px;height:28px"></span>Lumara</div>
  <p class="abs" style="left:620px;top:355px;width:440px;font-size:22px;font-weight:700;line-height:1.25">Lorem ipsum dolor sit amet, consectetur adipiscing elit, sed do eiusmod tempor incididunt</p>
  <div class="abs" style="left:620px;top:448px;width:400px;height:3px;background:#fff"></div>
</section>

<!-- Cover B -->
<section class="slide" style="left:39px;top:688px;width:1117px;height:627px">
  <svg class="abs" style="left:0;top:0" width="1117" height="627">
    <circle cx="250" cy="270" r="255" fill="var(--yellow)" opacity=".45"/>
    <circle cx="290" cy="360" r="255" fill="#cfcfcf"/>
    <circle cx="340" cy="300" r="255" fill="var(--teal)" opacity=".45"/>
  </svg>
  <div class="abs photo-night" role="img" aria-label="Night aerial view of a city with lit highway interchanges" style="left:48px;top:60px;width:500px;height:500px;border-radius:50%"></div>
  <div class="brand" style="left:632px;top:240px;font-size:34px;gap:12px"><span class="mark" style="width:28px;height:28px"></span>Lumara</div>
  <p class="abs" style="left:632px;top:345px;width:400px;font-size:20px;font-weight:700;line-height:1.25">Lorem ipsum dolor sit amet, consectetur adipiscing elit, sed do eiusmod tempor incididunt</p>
  <div class="abs" style="left:632px;top:438px;width:390px;height:3px;background:var(--teal)"></div>
</section>

<!-- Row 1 -->
<section class="slide col-l" style="top:1345px">
  <div class="abs photo-dusk" role="img" aria-label="Aerial landscape at golden sunset" style="inset:0"></div>
  <svg class="abs" style="left:0;top:0" width="549" height="310">
    <path d="M0 0 L0 310 L190 310 Q300 230 330 140 Q360 60 470 20 Q250 10 0 0 Z" fill="#fff"/>
    <path d="M0 0 Q120 40 210 20 Q140 60 0 50 Z" fill="var(--teal)" opacity=".6"/>
    <path d="M0 240 Q60 300 190 310 L0 310 Z" fill="var(--yellow)"/>
    <path d="M120 310 Q200 270 230 310 Z" fill="var(--green)"/>
  </svg>
  <div class="brand" style="left:352px;top:80px;font-size:17px;color:#fff;gap:6px"><span class="mark" style="width:14px;height:14px"></span>Lumara</div>
  <p class="abs" style="left:42px;top:162px;width:150px;font-size:9.5px;font-weight:700;line-height:1.25">Lorem ipsum dolor sit amet, consectetur adipiscing elit, sed do eiusmod tempor incididunt</p>
  <div class="abs" style="left:42px;top:214px;width:40px;height:2px;background:var(--teal)"></div>
</section>
<section class="slide col-r" style="top:1345px">
  <div class="abs photo-night" role="img" aria-label="City lights at night under a cloudy sky" style="inset:0"></div>
  <svg class="abs" style="left:0;top:0" width="549" height="310">
    <path d="M0 210 Q200 150 549 170 L549 310 L0 310 Z" fill="var(--yellow)" opacity=".9"/>
    <path d="M0 240 Q200 180 549 200 L549 310 L0 310 Z" fill="var(--green)"/>
  </svg>
  <div class="brand" style="left:24px;top:262px;font-size:13px;color:#fff;gap:5px"><span class="mark" style="width:11px;height:11px"></span>Lumara</div>
  <p class="abs" style="left:278px;top:238px;width:260px;font-size:9.5px;font-weight:700;line-height:1.2">Lorem ipsum dolor sit amet, consectetur adipiscing elit, sed do eiusmod tempor incididunt</p>
</section>

<!-- Row 2 -->
<section class="slide col-l" style="top:1682px">
  <div class="abs photo-city" role="img" aria-label="Hazy city skyline" style="inset:0"></div>
  <svg class="abs" style="left:0;top:0" width="549" height="310"><path d="M0 0 L170 0 Q190 110 90 120 Q30 125 0 160 Z" fill="var(--green)"/></svg>
  <div class="abs" style="left:16px;top:42px;font-size:26px;font-weight:900;color:#fff;letter-spacing:3px">INDEX</div>
  <div class="brand-mini" style="color:#fff"><span class="mark"></span>Lumara</div>
  <div class="num" style="left:180px;top:60px">1</div><div class="abs" style="left:206px;top:66px;font-size:8px;color:#fff;font-weight:700">About Us</div>
  <div class="num" style="left:180px;top:102px">2</div><div class="abs" style="left:206px;top:108px;font-size:8px;color:#fff;font-weight:700">Our Philosophy</div>
  <div class="num" style="left:180px;top:144px">3</div><div class="abs" style="left:206px;top:150px;font-size:8px;color:#fff;font-weight:700">Our Methodology</div>
  <div class="num" style="left:180px;top:186px">4</div><div class="abs" style="left:206px;top:192px;font-size:8px;color:#fff;font-weight:700">Our Main Services</div>
  <div class="num" style="left:180px;top:228px">5</div><div class="abs" style="left:206px;top:234px;font-size:8px;color:#fff;font-weight:700">Our Clients</div>
  <div class="num" style="left:352px;top:60px">6</div><div class="abs" style="left:378px;top:62px;font-size:8px;color:#fff;font-weight:700;width:100px">Why Choose Our Company</div>
  <div class="num" style="left:352px;top:102px">7</div><div class="abs" style="left:378px;top:108px;font-size:8px;color:#fff;font-weight:700">Training Areas</div>
  <div class="num" style="left:352px;top:144px">8</div><div class="abs" style="left:378px;top:150px;font-size:8px;color:#fff;font-weight:700">Custom Training</div>
  <div class="num" style="left:352px;top:186px">9</div><div class="abs" style="left:378px;top:192px;font-size:8px;color:#fff;font-weight:700">Contact Us Now</div>
</section>
<section class="slide col-r" style="top:1682px">
  <div class="accent acc-tl"><i class="a1"></i><i class="a2"></i><i class="a3"></i></div>
  <div class="title" style="font-size:14px">Welcome Message</div>
  <div class="brand-mini"><span class="mark"></span>Lumara</div>
  <div class="abs" role="img" aria-label="Portrait of the company CEO" style="left:231px;top:55px;width:86px;height:86px;border-radius:50%;border:4px solid var(--teal);background:linear-gradient(180deg,#d9dcd9,#8a9196)"></div>
  <div class="abs" style="left:0;width:549px;top:148px;text-align:center;font-size:7px;font-weight:900">AREN KALNS</div>
  <div class="abs" style="left:0;width:549px;top:160px;text-align:center;font-size:7px;font-weight:700">CEO</div>
  <div class="abs" style="left:0;top:187px;width:549px;height:123px;background:var(--green)"></div>
  <p class="abs" style="left:18px;top:208px;width:510px;font-size:6px;line-height:1.45;color:#fff">“ At vero eos et accusamus et iusto odio dignissimos ducimus qui blanditiis praesentium voluptatum deleniti atque corrupti quos dolores et quas molestias excepturi sint occaecati cupiditate non provident, similique sunt in culpa qui officia deserunt mollitia animi, id est laborum et dolorum fuga. Et harum quidem rerum facilis est et expedita distinctio. Nam libero tempore, cum soluta nobis est eligendi optio cumque nihil impedit quo minus id quod maxime placeat facere possimus, omnis dolor repellendus. ”</p>
</section>

<!-- Row 3 -->
<section class="slide col-l" style="top:2012px">
  <div class="accent acc-tl"><i class="a1"></i><i class="a2"></i><i class="a3"></i></div>
  <div class="title">Who We Are</div>
  <div class="brand-mini"><span class="mark"></span>Lumara</div>
  <p class="abs body" style="left:24px;top:85px;width:220px">Lorem ipsum dolor sit amet, consectetur adipiscing elit, sed do eiusmod tempor incididunt ut labore et dolore magna aliqua. Ut enim ad minim veniam, quis nostrud exercitation.<br><br>Sed ut perspiciatis unde omnis iste natus error sit voluptatem accusantium doloremque laudantium, totam rem aperiam, eaque ipsa quae ab illo inventore veritatis et quasi architecto beatae vitae dicta sunt explicabo. Nemo enim ipsam voluptatem quia voluptas sit aspernatur aut odit aut fugit, sed quia consequuntur magni dolores eos qui ratione voluptatem sequi nesciunt. Neque porro quisquam est, qui dolorem ipsum quia dolor sit amet, consectetur, adipisci velit, sed quia non numquam.</p>
  <svg class="abs" style="left:260px;top:0" width="289" height="310">
    <circle cx="150" cy="150" r="140" fill="var(--green-l)" opacity=".7"/>
    <circle cx="130" cy="160" r="118" fill="var(--yellow)" opacity=".6"/>
    <circle cx="150" cy="150" r="102" fill="#fff"/>
  </svg>
  <div class="abs photo-team" role="img" aria-label="Team gathered around a table in a meeting" style="left:320px;top:60px;width:180px;height:180px;border-radius:50%"></div>
</section>
<section class="slide col-r" style="top:2012px">
  <div class="abs" style="left:0;top:0;width:200px;height:310px;background:var(--green)"></div>
  <div class="abs photo-teal" role="img" aria-label="Hands working over documents and a laptop" style="left:60px;top:85px;width:175px;height:135px"></div>
  <div class="brand-mini" style="left:12px;right:auto;color:#fff"><span class="mark"></span>Lumara</div>
  <div class="title" style="left:auto;right:24px;font-size:14px">Our Mission</div>
  <div class="abs body" style="right:40px;top:70px;width:200px;text-align:right;line-height:1.4">
    <p style="margin-bottom:12px">Lorem ipsum dolor sit amet, consectetur</p>
    <p style="margin-bottom:12px">Sed ut perspiciatis unde omnis iste natus error sit voluptatem accusantium doloremque laudantium, totam rem aperiam, eaque ipsa</p>
    <p style="margin-bottom:12px">Nemo enim ipsam voluptatem quia voluptas sit aspernatur aut odit aut fugit, sed quia consequuntur magni dolores eos qui ratione</p>
    <p style="margin-bottom:12px">Neque porro quisquam est, qui dolorem ipsum quia dolor sit amet, consectetur</p>
    <p>Your texts goes here</p>
  </div>
  <svg class="abs" style="left:515px;top:78px" width="20" height="200">
    <circle cx="10" cy="5" r="5" fill="var(--green)"/><circle cx="10" cy="40" r="5" fill="var(--green)"/><circle cx="10" cy="88" r="5" fill="var(--green)"/><circle cx="10" cy="130" r="5" fill="var(--green)"/><circle cx="10" cy="163" r="5" fill="var(--green)"/>
  </svg>
</section>

<!-- Row 4 -->
<section class="slide col-l" style="top:2344px">
  <div class="accent acc-tl"><i class="a1"></i><i class="a2"></i><i class="a3"></i></div>
  <div class="title">Our Services</div>
  <p class="abs body" style="left:24px;top:55px;width:300px;font-size:7px">Lorem ipsum dolor sit amet, consectetur adipiscing elit, sed do eiusmod tempor incididunt ut labore et dolore magna aliqua. Ut enim ad minim veniam, quis nostrud exercitation ullamco laboris nisi ut aliquip ex ea commodo consequat. Duis aute irure dolor in reprehenderit</p>
  <div class="abs" style="left:24px;top:185px">
    <div class="check"><b></b>Lorem ipsum dolor sit</div><div class="check"><b></b>amet100% Lorem ipsum dolor</div><div class="check"><b></b>Lorem ipsum dolor si dolor</div><div class="check"><b class="dark"></b>Lorem ipsum dolor si dolor sit</div>
  </div>
  <div class="abs" style="left:180px;top:185px">
    <div class="check"><b></b>Lorem ipsum dolor sit</div><div class="check"><b class="dark"></b>amet100% Lorem ipsum dolor</div><div class="check"><b></b>Lorem ipsum dolor si dolor</div><div class="check"><b class="dark"></b>Lorem ipsum dolor si dolor sit</div>
  </div>
  <div class="abs" style="left:400px;top:0;width:149px;height:310px;background:repeating-linear-gradient(90deg,var(--green-d) 0 14px,#2f4d1a 14px 22px,var(--green) 22px 36px)"></div>
  <div class="abs photo-team" role="img" aria-label="Business people shaking hands in an office" style="left:340px;top:105px;width:200px;height:130px"></div>
  <div class="brand-mini" style="color:#fff"><span class="mark"></span>Lumara</div>
</section>
<section class="slide col-r" style="top:2344px">
  <div class="abs" style="left:0;top:0;width:549px;height:155px;background:var(--green)"></div>
  <div class="title" style="color:#fff;font-size:14px">Title Goes Here</div>
  <div class="brand-mini" style="color:#fff"><span class="mark"></span>Lumara</div>
  <div class="abs" style="left:80px;top:107px;width:66px;height:66px;border-radius:50%;background:var(--teal);border:4px solid #fff;color:#fff;font-size:7px;font-weight:700;display:flex;align-items:flex-end;justify-content:center;padding-bottom:12px">Efficiency</div>
  <div class="abs" style="left:240px;top:107px;width:66px;height:66px;border-radius:50%;background:var(--ink);border:4px solid #fff;color:#fff;font-size:7px;font-weight:700;display:flex;align-items:flex-end;justify-content:center;padding-bottom:12px">Proactive</div>
  <div class="abs" style="left:390px;top:107px;width:66px;height:66px;border-radius:50%;background:var(--yellow);border:4px solid #fff;color:#fff;font-size:6px;font-weight:700;display:flex;align-items:flex-end;justify-content:center;padding-bottom:10px;text-align:center">Multi-Channel Development</div>
  <p class="abs body" style="left:78px;top:186px;width:80px;font-size:5.5px">Using our expertise and in-depth knowledge, we develop cost effective and comprehensive e-learning courses.</p>
  <p class="abs body" style="left:220px;top:186px;width:100px;font-size:5.5px;text-align:center">Regardless of how complex is your system, our mission is to engage your audience by developing high-impact solutions.</p>
  <p class="abs body" style="left:378px;top:186px;width:95px;font-size:5.5px">Using our expertise and in-depth knowledge, we develop cost effective and comprehensive e-learning courses.</p>
</section>

<!-- Row 5 -->
<section class="slide col-l" style="top:2677px">
  <div class="abs" style="left:0;top:0;width:549px;height:135px;background:var(--green)"></div>
  <div class="title" style="color:#fff">What We Offer</div>
  <div class="brand-mini" style="color:#fff"><span class="mark"></span>Lumara</div>
  <div class="abs" role="img" aria-label="Digital learning concept on a laptop" style="left:36px;top:108px;width:135px;height:78px;border-radius:12px;border:3px solid #fff;background:linear-gradient(135deg,#f0c86a,#c08a3a)"></div>
  <div class="abs" role="img" aria-label="Blue glowing laptop keyboard" style="left:205px;top:108px;width:135px;height:78px;border-radius:12px;border:3px solid #fff;background:linear-gradient(135deg,#1c3c8a,#0b1a3c)"></div>
  <div class="abs" role="img" aria-label="Business charts on a desk" style="left:374px;top:108px;width:135px;height:78px;border-radius:12px;border:3px solid #fff;background:linear-gradient(135deg,#f5d98a,#c0a050)"></div>
  <div class="abs" style="left:36px;top:196px;width:135px;font-size:7px;font-weight:900;text-align:center">Lorem Ipsum</div>
  <div class="abs" style="left:205px;top:196px;width:135px;font-size:7px;font-weight:900;text-align:center">Lorem Ipsum</div>
  <div class="abs" style="left:374px;top:196px;width:135px;font-size:7px;font-weight:900;text-align:center">Lorem Ipsum</div>
  <p class="abs body" style="left:40px;top:208px;width:130px;font-size:5.5px">Lorem ipsum dolor sit amet, consectetur adipiscing elit, sed do eiusmod tempor incididunt ut labore et dolore magna aliqua. Ut enim ad minim veniam</p>
  <p class="abs body" style="left:209px;top:208px;width:130px;font-size:5.5px">Lorem ipsum dolor sit amet, consectetur adipiscing elit, sed do eiusmod tempor incididunt ut labore et dolore magna aliqua. Ut enim ad minim veniam</p>
  <p class="abs body" style="left:378px;top:208px;width:130px;font-size:5.5px">Lorem ipsum dolor sit amet, consectetur adipiscing elit, sed do eiusmod tempor incididunt ut labore et dolore magna aliqua. Ut enim ad minim veniam</p>
  <div class="accent acc-br"><i class="a1"></i><i class="a2"></i><i class="a3"></i></div>
</section>
<section class="slide col-r" style="top:2677px">
  <div class="abs" style="left:370px;top:0;width:179px;height:310px;background:var(--green)"></div>
  <div class="accent acc-tl"><i class="a1"></i><i class="a2"></i><i class="a3"></i></div>
  <div class="title" style="font-size:14px">Our Clients</div>
  <div class="brand-mini" style="color:#fff"><span class="mark"></span>Lumara</div>
  <div class="abs" style="left:28px;top:82px;width:250px;height:190px;border:1px solid #999"></div>
  <p class="abs body" style="left:40px;top:92px;width:228px;font-size:5.5px">Lorem Ipsum is simply dummy text of the printing and typesetting industry. Lorem Ipsum has been<br><br>The industry's standard dummy text ever since the 1500s, when an unknown printer took a galley of type and scrambled it to make a type specimen book.<br><br>It has survived not only five centuries, but also the leap into electronic typesetting, remaining essentially unchanged. It was popularised in the 1960s with the release of sheets containing Lorem Ipsum passages, and more recently with desktop publishing software including versions of Lorem Ipsum.<br><br>It has survived not only five centuries, but also the leap into electronic typesetting, remaining essentially unchanged. It was</p>
  <svg class="abs" style="left:300px;top:70px" width="240" height="200">
    <circle cx="120" cy="100" r="80" fill="none" stroke="var(--teal)" stroke-width="26"/>
    <circle cx="120" cy="100" r="80" fill="none" stroke="#ccc" stroke-width="26" stroke-dasharray="120 400" transform="rotate(150 120 100)"/>
  </svg>
  <div class="abs" style="left:322px;top:100px;width:62px;height:22px;border-radius:4px;background:#fff;border:1px solid #888;font-size:9px;font-weight:900;display:flex;align-items:center;justify-content:center">LOGO</div>
  <div class="abs" style="left:300px;top:170px;width:62px;height:22px;border-radius:4px;background:#fff;border:1px solid #888;font-size:9px;font-weight:900;display:flex;align-items:center;justify-content:center">LOGO</div>
  <div class="abs" style="left:452px;top:144px;width:62px;height:22px;border-radius:4px;background:#fff;border:1px solid #888;font-size:9px;font-weight:900;display:flex;align-items:center;justify-content:center;color:var(--teal)">LOGO</div>
  <div class="abs" style="left:452px;top:200px;width:62px;height:22px;border-radius:4px;background:#fff;border:1px solid #888;font-size:9px;font-weight:900;display:flex;align-items:center;justify-content:center;color:var(--teal)">LOGO</div>
</section>

<!-- Row 6 -->
<section class="slide col-l" style="top:3009px">
  <div class="abs" style="left:0;top:0;width:549px;height:110px;background:var(--green)"></div>
  <div class="title" style="color:#fff;top:14px">Financing</div>
  <div class="brand-mini" style="color:#fff"><span class="mark"></span>Lumara</div>
  <svg class="abs" style="left:36px;top:85px;background:#fff;box-shadow:0 1px 4px rgba(0,0,0,.2)" width="480" height="85">
    <g stroke="#e3e3e3" stroke-width=".5"><line x1="20" y1="12" x2="470" y2="12"/><line x1="20" y1="40" x2="470" y2="40"/><line x1="20" y1="68" x2="470" y2="68"/></g>
    <g font-size="5" fill="#666"><text x="6" y="14">100</text><text x="8" y="42">50</text><text x="12" y="70">0</text></g>
    <polyline fill="none" stroke="#111" stroke-width="1.2" points="40,50 95,56 150,54 205,32 260,26 315,34 370,38 425,30"/>
    <polyline fill="none" stroke="var(--yellow)" stroke-width="1.2" points="40,44 95,42 150,50 205,40 260,42 315,40 370,44 425,38"/>
    <g font-size="5" fill="#333"><text x="150" y="80">— Series 1</text><text x="210" y="80" fill="#c9a010">— Series 2</text></g>
  </svg>
  <div class="abs" style="left:36px;top:190px;width:480px">
    <table class="fin">
      <tr class="h"><td>Category Name-01</td><td>Category Name-02</td><td>Category Name-03</td><td>Category Name-04</td><td>Category Name-05</td></tr>
      <tr><td>Lorem Ipsum</td><td>0.00</td><td>0.00</td><td>0.00</td><td>0.00</td></tr>
      <tr><td>Lorem Ipsum</td><td>0.00</td><td>0.00</td><td>0.00</td><td>0.00</td></tr>
      <tr class="t"><td>Total=</td><td>0.00</td><td>0.00</td><td>0.00</td><td>0.00</td></tr>
    </table>
  </div>
</section>
<section class="slide col-r" style="top:3009px">
  <div class="accent acc-tl"><i class="a1"></i><i class="a2"></i><i class="a3"></i></div>
  <div class="title" style="font-size:14px">Financing</div>
  <svg class="abs" style="left:0;top:0" width="549" height="310"><path d="M330 0 L549 0 L549 310 L250 310 Q360 200 330 0 Z" fill="var(--green)"/><path d="M300 0 L340 0 Q370 180 260 310 L230 310 Q340 180 300 0Z" fill="var(--teal)" opacity=".5"/></svg>
  <div class="brand-mini" style="color:#fff"><span class="mark"></span>Lumara</div>
  <svg class="abs" style="left:10px;top:70px" width="280" height="220">
    <g font-size="4.5" fill="#666"><text x="0" y="10">$120,000,000</text><text x="0" y="35">$100,000,000</text><text x="0" y="60">$80,000,000</text><text x="0" y="85">$60,000,000</text><text x="0" y="110">$40,000,000</text><text x="0" y="135">$20,000,000</text><text x="20" y="160">$0</text></g>
    <rect x="70" y="70" width="14" height="88" fill="var(--green)"/><rect x="86" y="128" width="6" height="30" fill="var(--yellow)"/>
    <rect x="145" y="50" width="14" height="108" fill="var(--green)"/><rect x="161" y="122" width="6" height="36" fill="var(--yellow)"/>
    <rect x="220" y="45" width="14" height="113" fill="var(--green)"/><rect x="236" y="110" width="6" height="48" fill="var(--yellow)"/>
    <g font-size="5" font-weight="700" fill="#333"><text x="60" y="66">$78,000,000</text><text x="135" y="46">$89,456,323</text><text x="210" y="41">$95,320,891</text>
    <text x="70" y="168">Year-01</text><text x="145" y="168">Year-02</text><text x="220" y="168">Year-03</text></g>
    <g font-size="4.5" fill="#333"><text x="130" y="180">■ Earning  ■ Profit</text></g>
  </svg>
  <p class="abs" style="left:370px;top:55px;width:160px;font-size:9px;font-weight:700;color:#fff">The estimates obtained from the financial plan show:</p>
  <div class="abs" style="left:345px;top:130px;width:20px;height:20px;border-radius:50%;background:#fff;border:2px solid var(--teal)"></div>
  <p class="abs" style="left:375px;top:128px;width:150px;font-size:5px;color:#fff">Lorem ipsum dolor sit amet, consectetur adipiscing elit, sed do eiusmod tempor</p>
  <div class="abs" style="left:345px;top:166px;width:20px;height:20px;border-radius:50%;background:#fff;border:2px solid var(--teal)"></div>
  <p class="abs" style="left:375px;top:164px;width:150px;font-size:5px;color:#fff">Lorem ipsum dolor sit amet, consectetur adipiscing elit, sed do eiusmod tempor</p>
  <div class="abs" style="left:345px;top:202px;width:20px;height:20px;border-radius:50%;background:#fff;border:2px solid var(--yellow)"></div>
  <p class="abs" style="left:375px;top:200px;width:150px;font-size:5px;color:#fff">Lorem ipsum dolor sit amet, consectetur adipiscing elit, sed do eiusmod tempor</p>
</section>

<!-- Row 7 -->
<section class="slide col-l" style="top:3341px">
  <div class="accent acc-tl"><i class="a1"></i><i class="a2"></i><i class="a3"></i></div>
  <div class="title">Our Philosophy</div>
  <div class="abs" style="left:265px;top:0;width:284px;height:310px;background:var(--green)"></div>
  <div class="brand-mini" style="color:#fff"><span class="mark"></span>Lumara</div>
  <div class="abs" style="left:50px;top:105px;width:30px;height:60px;background:var(--green)"></div>
  <div class="abs" style="left:198px;top:180px;width:30px;height:90px;background:var(--yellow)"></div>
  <div class="abs" role="img" aria-label="Hand holding a glass sphere reflecting trees" style="left:65px;top:85px;width:155px;height:190px;background:linear-gradient(160deg,#c8b79a,#6d6356 50%,#2f3b44)"></div>
  <svg class="abs" style="left:278px;top:45px" width="40" height="250">
    <circle cx="20" cy="25" r="15" fill="var(--teal)" stroke="#fff" stroke-width="2"/><circle cx="20" cy="85" r="15" fill="#c9a21a" stroke="#fff" stroke-width="2"/><circle cx="20" cy="152" r="15" fill="var(--teal)" stroke="#fff" stroke-width="2"/><circle cx="20" cy="220" r="15" fill="#c9a21a" stroke="#fff" stroke-width="2"/>
    <g fill="#fff" font-size="12" font-weight="700" text-anchor="middle"><text x="20" y="30">1</text><text x="20" y="90">2</text><text x="20" y="157">3</text><text x="20" y="225">4</text></g>
  </svg>
  <div class="abs" style="left:330px;top:60px;width:200px;color:#fff;font-size:9px;font-weight:700">Philosophy Name - 1<p style="font-size:5.5px;font-weight:400;color:var(--yellow)">Lorem ipsum dolor sit amet, consectetur adipiscing elit, sed do eiusmod tempor</p></div>
  <div class="abs" style="left:330px;top:120px;width:200px;color:#fff;font-size:9px;font-weight:700">Philosophy Name - 1<p style="font-size:5.5px;font-weight:400;color:var(--yellow)">Lorem ipsum dolor sit amet, consectetur adipiscing elit, sed do eiusmod tempor</p></div>
  <div class="abs" style="left:330px;top:187px;width:200px;color:#fff;font-size:9px;font-weight:700">Philosophy Name - 1<p style="font-size:5.5px;font-weight:400;color:var(--yellow)">Lorem ipsum dolor sit amet, consectetur adipiscing elit, sed do eiusmod tempor</p></div>
  <div class="abs" style="left:330px;top:255px;width:200px;color:#fff;font-size:9px;font-weight:700">Philosophy Name - 1<p style="font-size:5.5px;font-weight:400;color:var(--yellow)">Lorem ipsum dolor sit amet, consectetur adipiscing elit, sed do eiusmod tempor</p></div>
</section>
<section class="slide col-r" style="top:3341px">
  <div class="accent acc-tl"><i class="a1"></i><i class="a2"></i><i class="a3"></i></div>
  <div class="title" style="font-size:14px">Our Strategy</div>
  <div class="brand-mini"><span class="mark"></span>Lumara</div>
  <svg class="abs" style="left:0;top:0" width="549" height="310">
    <path d="M160 130 Q170 250 260 250" fill="none" stroke="#e2efcf" stroke-width="22"/>
    <path d="M290 250 Q380 250 390 150" fill="none" stroke="var(--green-l)" stroke-width="22"/>
    <path d="M370 140 Q380 60 300 45 L310 30 L260 50 L305 78 L300 62 Q355 72 350 140Z" fill="var(--green)"/>
    <circle cx="260" cy="150" r="36" fill="var(--yellow)"/><circle cx="260" cy="150" r="28" fill="#fff"/>
    <path d="M250 140 a10 10 0 1 1 20 0 q0 6-5 10 v6 h-10 v-6 q-5-4-5-10z M252 160 h16 v4 h-16z" fill="var(--ink)"/>
    <g fill="#fff" stroke="var(--teal)" stroke-width="2"><circle cx="130" cy="140" r="12"/><circle cx="185" cy="230" r="12"/><circle cx="295" cy="245" r="12"/><circle cx="367" cy="175" r="12"/><circle cx="383" cy="75" r="12"/></g>
  </svg>
  <div class="abs" style="left:60px;top:85px;width:80px;text-align:center;font-size:6px;font-weight:900">Strategy: 01<p class="body" style="font-size:4.5px;font-weight:400">Lorem ipsum dolor sit amet consectetur adipiscing elit sed do eiusmod</p></div>
  <div class="abs" style="left:80px;top:250px;width:80px;text-align:center;font-size:6px;font-weight:900">Strategy: 02<p class="body" style="font-size:4.5px;font-weight:400">Lorem ipsum dolor sit amet consectetur adipiscing elit sed do eiusmod</p></div>
  <div class="abs" style="left:400px;top:250px;width:80px;text-align:center;font-size:6px;font-weight:900">Strategy: 03<p class="body" style="font-size:4.5px;font-weight:400">Lorem ipsum dolor sit amet consectetur adipiscing elit sed do eiusmod</p></div>
  <div class="abs" style="left:420px;top:160px;width:90px;text-align:right;font-size:6px;font-weight:900">Strategy: 04<p class="body" style="font-size:4.5px;font-weight:400">Lorem ipsum dolor sit amet consectetur adipiscing elit sed do eiusmod</p></div>
  <div class="abs" style="left:420px;top:62px;width:90px;text-align:right;font-size:6px;font-weight:900">Strategy: 05<p class="body" style="font-size:4.5px;font-weight:400">Lorem ipsum dolor sit amet consectetur adipiscing elit sed do eiusmod</p></div>
  <div class="accent acc-br"><i class="a1"></i><i class="a2"></i><i class="a3"></i></div>
</section>

<!-- Row 8 -->
<section class="slide col-l" style="top:3680px">
  <div class="accent acc-tl"><i class="a1"></i><i class="a2"></i><i class="a3"></i></div>
  <div class="title">Our Strategy</div>
  <div class="brand-mini"><span class="mark"></span>Lumara</div>
  <svg class="abs" style="left:0;top:0" width="549" height="310">
    <circle cx="280" cy="158" r="90" fill="none" stroke="#7a3fb5" stroke-width="1.2" stroke-dasharray="3 3"/>
    <circle cx="280" cy="158" r="64" fill="#f3f0d8"/>
    <g fill="#fff" stroke="var(--green)" stroke-width="2"><circle cx="275" cy="70" r="13"/><circle cx="348" cy="110" r="13"/><circle cx="348" cy="205" r="13"/><circle cx="275" cy="248" r="13"/><circle cx="208" cy="205" r="13"/><circle cx="208" cy="110" r="13"/></g>
    <g font-size="18" font-weight="400" fill="#333"><text x="238" y="47">1</text><text x="382" y="116">2</text><text x="382" y="212">3</text><text x="301" y="276">4</text><text x="165" y="212">5</text><text x="165" y="116">6</text></g>
  </svg>
  <div class="abs" style="left:216px;top:136px;width:128px;text-align:center;font-size:15px;font-weight:900;line-height:1.2"><span style="color:var(--green)">Competitor</span><br>Analysis</div>
  <p class="abs body" style="left:260px;top:32px;width:80px;font-size:5px">Lorem ipsum dolor sit amet, consectetur</p>
  <p class="abs body" style="left:398px;top:104px;width:80px;font-size:5px">Lorem ipsum dolor sit amet, consectetur</p>
  <p class="abs body" style="left:398px;top:200px;width:80px;font-size:5px">Lorem ipsum dolor sit amet, consectetur</p>
  <p class="abs body" style="left:318px;top:266px;width:80px;font-size:5px">Lorem ipsum dolor sit amet, consectetur</p>
  <p class="abs body" style="left:78px;top:200px;width:80px;font-size:5px;text-align:right">Lorem ipsum dolor sit amet, consectetur</p>
  <p class="abs body" style="left:78px;top:104px;width:80px;font-size:5px;text-align:right">Lorem ipsum dolor sit amet, consectetur</p>
  <div class="accent acc-br"><i class="a1"></i><i class="a2"></i><i class="a3"></i></div>
</section>
<section class="slide col-r" style="top:3680px">
  <div class="accent acc-tl"><i class="a1"></i><i class="a2"></i><i class="a3"></i></div>
  <div class="title" style="font-size:14px">Infographic Style</div>
  <div class="brand-mini"><span class="mark"></span>Lumara</div>
  <svg class="abs" style="left:0;top:0" width="549" height="310">
    <g stroke="#fff" stroke-width="3">
      <polygon points="118,80 140,92 140,118 118,130 96,118 96,92" fill="var(--green)"/>
      <polygon points="218,80 240,92 240,118 218,130 196,118 196,92" fill="var(--yellow)"/>
      <polygon points="318,80 340,92 340,118 318,130 296,118 296,92" fill="var(--teal)"/>
      <polygon points="418,80 440,92 440,118 418,130 396,118 396,92" fill="#5d8c2a"/>
    </g>
    <g fill="none" stroke="#fff" stroke-width="2"><circle cx="118" cy="105" r="9"/><path d="M113 105 l4 4 l7-8"/><circle cx="218" cy="105" r="9"/><path d="M318 96 v9 h9"/><circle cx="318" cy="105" r="9"/><circle cx="418" cy="105" r="8" stroke-dasharray="3 2"/><circle cx="418" cy="105" r="3"/></g>
    <rect x="70" y="143" width="400" height="8" fill="#4a4a4a"/><polygon points="470,137 485,147 470,157" fill="#4a4a4a"/>
    <g fill="#4a4a4a"><polygon points="112,151 124,151 118,160"/><polygon points="212,151 224,151 218,160"/><polygon points="312,151 324,151 318,160"/><polygon points="412,151 424,151 418,160"/></g>
  </svg>
  <div class="abs" style="left:78px;top:166px;width:80px;text-align:center;font-size:6.5px;font-weight:700;color:var(--green)">Lorem Ipsum</div>
  <div class="abs" style="left:178px;top:166px;width:80px;text-align:center;font-size:6.5px;font-weight:700;color:var(--yellow)">Lorem Ipsum</div>
  <div class="abs" style="left:278px;top:166px;width:80px;text-align:center;font-size:6.5px;font-weight:700;color:var(--teal)">Lorem Ipsum</div>
  <div class="abs" style="left:378px;top:166px;width:80px;text-align:center;font-size:6.5px;font-weight:700;color:#5d8c2a">Lorem Ipsum</div>
  <p class="abs body" style="left:84px;top:178px;width:70px;font-size:5px">Ipsum dolor sit amet, consectetur adipiscing elit, sed do eiusmod tempor incididunt ut labore et dolore magna aliqua</p>
  <p class="abs body" style="left:184px;top:178px;width:70px;font-size:5px">Ipsum dolor sit amet, consectetur adipiscing elit, sed do eiusmod tempor incididunt ut labore et dolore magna aliqua</p>
  <p class="abs body" style="left:284px;top:178px;width:70px;font-size:5px">Ipsum dolor sit amet, consectetur adipiscing elit, sed do eiusmod tempor incididunt ut labore et dolore magna aliqua</p>
  <p class="abs body" style="left:384px;top:178px;width:70px;font-size:5px">Ipsum dolor sit amet, consectetur adipiscing elit, sed do eiusmod tempor incididunt ut labore et dolore magna aliqua</p>
  <div class="accent acc-br"><i class="a1"></i><i class="a2"></i><i class="a3"></i></div>
</section>

<!-- Row 9 -->
<section class="slide col-l" style="top:4015px">
  <div class="accent acc-tl"><i class="a1"></i><i class="a2"></i><i class="a3"></i></div>
  <div class="title">Diagram Process</div>
  <div class="brand-mini"><span class="mark"></span>Lumara</div>
  <div class="abs" style="left:0;top:112px;width:549px;height:198px;background:#c5e39f"></div>
  <div class="proc" style="left:40px;top:82px;width:107px;background:#fff;color:#333;box-shadow:0 1px 3px rgba(0,0,0,.2)">Your Text Goes Here</div>
  <div class="proc" style="left:165px;top:82px;width:107px;background:#fff;color:#333;box-shadow:0 1px 3px rgba(0,0,0,.2)">Your Text Goes Here</div>
  <div class="proc" style="left:290px;top:82px;width:107px;background:#fff;color:#333;box-shadow:0 1px 3px rgba(0,0,0,.2)">Your Text Goes Here</div>
  <div class="proc" style="left:415px;top:82px;width:107px;background:#fff;color:#333;box-shadow:0 1px 3px rgba(0,0,0,.2)">Your Text Goes Here</div>
  <div class="proc" style="left:40px;top:122px;width:107px;background:var(--teal)">Your Text Goes Here</div>
  <div class="proc" style="left:40px;top:162px;width:107px;background:var(--teal)">Your Text Goes Here</div>
  <div class="proc" style="left:165px;top:122px;width:107px;background:var(--green)">Your Text Goes Here</div>
  <div class="proc" style="left:165px;top:162px;width:107px;background:var(--green)">Your Text Goes Here</div>
  <div class="proc" style="left:165px;top:202px;width:107px;background:var(--green)">Your Text Goes Here</div>
  <div class="proc" style="left:290px;top:122px;width:107px;background:var(--yellow)">Your Text Goes Here</div>
  <div class="proc" style="left:290px;top:162px;width:107px;background:var(--yellow)">Your Text Goes Here</div>
  <div class="proc" style="left:290px;top:202px;width:107px;background:var(--yellow)">Your Text Goes Here</div>
  <div class="proc" style="left:290px;top:242px;width:107px;background:var(--yellow)">Your Text Goes Here</div>
  <div class="proc" style="left:415px;top:122px;width:107px;background:var(--green-d)">Your Text Goes Here</div>
  <svg class="abs" style="left:0;top:0" width="549" height="310">
    <g fill="var(--ink)"><polygon points="87,184 99,184 93,194"/><polygon points="212,224 224,224 218,234"/><polygon points="337,264 349,264 343,274"/><polygon points="462,144 474,144 468,154"/></g>
  </svg>
</section>

</div>
</body>
</html>
```